Mail - Scan, Sort & Forward - Web Design

We need a web design for a mail scan, store, view and forward service. It is a lifestyle service predicated on freedom, convenience, ease of access, ease of use, security, safety. It involves personal information and is accessed remotely.
No branding or style guide is yet complete so an open pallet is available but design should convey simplicity as it targets demographic 45-75 years travellers but also high net worth multi location professionals, miners and other multi-location workers.
Competitor sites are: (for business description examples)
www.quellarbox.example
www.trimbeldesk.example.au
www.norvandelsupply.example.au
Updates

Attached files are wireframes which show how the service will work (UI). You should use these to form ideas about your web design for the service. They are not templates nor am I looking for a UI dev (yet).

Target Market(s)

Travellers ( especially retirees) and multi-location workers eg miners

Industry/Entity Type

Business

Requirements
Must have
• Being a lifestyle site, the pages must be low on text, lite layout, imagery addressing the target market.
Navigation should be simple to use
Concept of visitor / member / client should be addressed. The user needs to be able to permission other user groups (read-only)
Talk to reasons why prospects want to use this service.
Nice to have
• access to view nearest Kelm Rout office.
Regular call to action like survey, quiz or did you know info which may keep the user returning to the site.
Campaign section which enables customising of campaigns on an ongoing basis
Ability to access and download Terms & conditions, brochures .pdf or other information.
Simulate how service works..video or webcast
Should not have
• Do not want heavy or dense text everywhere. Use imagery where possible. Icons should be thematic not isolated.

```html
<!DOCTYPE html>
<html lang="en">
<head>
<meta charset="utf-8">
<title>Parcelwind.au – Mail Scan, Store &amp; Forward</title>
<link href="https://fonts.googleapis.com/css2?family=Exo+2:wght@300&family=PT+Sans:wght@400;700&display=swap" rel="stylesheet">
<style>
:root{
  --ink:#1f2428;
  --text:#222;
  --muted:#777;
  --line:#cfcfcf;
  --panel:#e7e7e7;
  --brand:#1a7fd8;
  --link:#1a8ad6;
  --alert:#d8261c;
  --sea-deep:#1565b8;
  --sea-light:#a8e2f7;
}
*{box-sizing:border-box;margin:0;padding:0}
html,body{width:1159px;height:1200px;overflow:hidden;background:#fff}
body{position:relative;font-family:"PT Sans",Arial,sans-serif;color:var(--text)}
.abs{position:absolute}

.brand-mark{left:47px;top:22px;width:74px;height:74px;background:var(--ink)}
.brand-name{left:168px;top:36px;font-family:"Exo 2",Arial,sans-serif;font-weight:300;font-size:52px;color:var(--brand);letter-spacing:-.5px}

.main-nav{left:609px;top:99px;width:499px;height:36px;border:1px solid #d4d4d4;border-bottom:none;background:linear-gradient(#fff,#e9e9e9);display:flex;align-items:center;font-size:15px}
.main-nav a{color:var(--text);text-decoration:none;position:absolute;top:8px;letter-spacing:-.2px}

.hero{left:41px;top:135px;width:1067px;height:324px;background:linear-gradient(180deg,var(--sea-light) 0%,#5cc3ee 38%,#2a92d6 60%,var(--sea-deep) 100%)}

.member-nav{left:41px;top:459px;width:1067px;height:41px;background:var(--ink);border-radius:0 0 4px 4px;color:#fff;font-size:15px;letter-spacing:-.2px}
.member-nav span{position:absolute;top:11px;white-space:nowrap}

.content{left:42px;top:508px;width:1062px;height:630px;border:1px solid #ddd;border-bottom:none}

.mail-col{top:519px;height:304px;border:1px solid var(--line);background:#fff}
.mail-col h3{height:26px;font-weight:400;font-size:15px;text-align:center;line-height:26px;background:linear-gradient(#fff,#ececec);border-bottom:1px solid var(--line);color:var(--text);letter-spacing:-.2px}
.mail-col ul{list-style:none}
.mail-col li{height:31px;line-height:31px;text-align:center;font-size:12.5px;color:var(--muted);border-bottom:1px solid #e3e3e3;letter-spacing:.2px;white-space:nowrap}
.mail-col li:last-child{border-bottom:none}

.video{left:52px;top:852px;width:411px;height:245px;background:linear-gradient(#2f86c6,#135e9f);padding:8px}
.video-screen{width:100%;height:203px;background:#000;position:relative}
.play-btn{position:absolute;left:170px;top:78px;width:68px;height:46px;border-radius:8px;background:linear-gradient(#d8d8d8,#8a8a8a);border:2px solid #555}
.play-btn svg{position:absolute;left:22px;top:11px}
.video-bar{height:24px;margin-top:2px;background:linear-gradient(#3a3a3a,#111);display:flex;align-items:center;padding:0 8px;gap:8px;color:#fff;font-size:10px}
.track{flex:1;height:8px;border-radius:4px;background:#ccc}

.download{left:486px;width:305px;border:1px solid #d6d6d6;background:#ececec;padding:10px 10px 10px 11px;font-size:12.5px;line-height:17.5px;color:#333;letter-spacing:-.25px}
.download .cta{position:absolute;color:var(--alert);white-space:nowrap}
.doc-icon{position:absolute;width:36px;height:40px;background:#b42418}

.side-panel{left:813px;width:279px}
.side-head{height:42px;background:var(--ink);color:#fff;font-size:19px;line-height:42px;letter-spacing:-.2px}
.survey-body{background:var(--panel);height:233px;position:relative;padding:14px 0 0 32px}
.survey-body p{font-size:16px;margin-bottom:10px;letter-spacing:-.3px}
.survey-body li{list-style:none;font-size:15px;height:28.5px;display:flex;align-items:center;gap:10px;margin-left:2px;letter-spacing:-.2px}
.survey-body li::before{content:"";width:11px;height:11px;border-radius:50%;background:var(--ink)}
.submit{position:absolute;left:107px;top:193px;width:107px;height:31px;background:linear-gradient(#4a4a4a,#111);color:#fff;font-size:16px;text-align:center;line-height:30px;border:1px solid #000}

.promo-body{border:1px solid #ccc;border-top:none;height:245px;padding-top:16px}
.promo-item{position:relative;height:80px;padding-left:70px}
.promo-item .thumb{position:absolute;left:10px;top:2px;width:50px;height:40px;border-radius:4px;background:linear-gradient(#e4eef4,#9fb3c1)}
.promo-item h4{font-size:12px;color:var(--link);font-weight:700;margin-bottom:2px}
.promo-item p{font-size:11px;color:#999;line-height:16px;width:200px;letter-spacing:-.1px}

.footer{left:0;top:1134px;width:1159px;height:66px;background:var(--ink);color:#fff;font-size:12.5px;text-align:center;line-height:66px;letter-spacing:-.2px}
</style>
</head>
<body>

<header>
  <div class="abs brand-mark"></div>
  <div class="abs brand-name">Parcelwind.au</div>
  <nav class="abs main-nav">
    <a style="left:21px">Home</a>
    <a style="left:94px">About Us</a>
    <a style="left:188px">Pricing</a>
    <a style="left:268px">Services</a>
    <a style="left:351px">FAQ</a>
    <a style="left:403px">Contact Us</a>
  </nav>
</header>

<div class="abs hero" role="img" aria-label="Ocean wave splash with a seagull in flight and a large glass @ symbol rising from the water"></div>

<nav class="abs member-nav">
  <span style="left:21px">New Postal Mail</span>
  <span style="left:169px">Achive Postal Mail</span>
  <span style="left:328px">Document Vault</span>
  <span style="left:475px">User Profile &amp; Access</span>
  <span style="left:657px">Account History</span>
</nav>

<main>
  <div class="abs content"></div>

  <section class="abs mail-col" style="left:54px;width:123px">
    <h3>Date Recorded</h3>
    <ul><li>25 Feb 2009</li><li>25 Feb 2009</li><li>25 Feb 2009</li><li>25 Feb 2009</li><li>25 Feb 2009</li><li>25 Feb 2009</li><li>25 Feb 2009</li><li>25 Feb 2009</li><li>25 Feb 2009</li></ul>
  </section>
  <section class="abs mail-col" style="left:184px;width:126px">
    <h3>Document Type</h3>
    <ul><li>Invoice</li><li>Restricted</li><li>Prospectus</li><li>Invoice</li><li>Restricted</li><li>Prospectus</li><li>Invoice</li><li>Restricted</li><li>Prospectus</li></ul>
  </section>
  <section class="abs mail-col" style="left:319px;width:177px">
    <h3>Scan/Not Scan</h3>
    <ul><li>Scanned</li><li>Client Request/Not Scanned</li><li>Too Large/Not Scanned</li><li>Scanned</li><li>Not Scanned</li><li>Client Request/Not Scanned</li><li>Scanned</li><li>Not Scanned</li><li>Client Request/Not Scanned</li></ul>
  </section>
  <section class="abs mail-col" style="left:507px;width:155px">
    <h3>Document Name</h3>
    <ul><li>Document Name</li><li>Document Name</li><li>Document Name</li><li>Document Name</li><li>Document Name</li><li>Document Name</li><li>Document Name</li><li>Document Name</li><li>Document Name</li></ul>
  </section>
  <section class="abs mail-col" style="left:673px;width:118px">
    <h3>Sender</h3>
    <ul><li>Supplier Name</li><li>Ormund - Gas</li><li>Letter From John</li><li>Tarrow</li><li>Supplier Name</li><li>Ormund - Gas</li><li>Letter From John</li><li>Tarrow</li><li></li></ul>
  </section>

  <div class="abs video">
    <div class="video-screen">
      <div class="play-btn"><svg width="22" height="22" viewBox="0 0 22 22"><path d="M3 1 L20 11 L3 21Z" fill="#333"/></svg></div>
    </div>
    <div class="video-bar">
      <svg width="12" height="12" viewBox="0 0 12 12"><path d="M1 0 L11 6 L1 12Z" fill="#fff"/></svg>
      <div class="track"></div>
      <span>0:00 / 0:00</span>
    </div>
  </div>

  <section class="abs download" style="top:854px;height:109px">
    <p>Lorem ipsum dolor sit amet, consectetur adipisicing elit, sed do eiusmod tempo Lorem ipsum dolor sit amet, consectetur adipisicing elit....</p>
    <span class="cta" style="right:50px;top:77px;font-size:17px">DOWNLOAD PDF</span>
    <span class="doc-icon" style="left:260px;top:60px"></span>
  </section>
  <section class="abs download" style="top:976px;height:121px">
    <p>Lorem ipsum dolor sit amet, consectetur adipisicing elit, sed do eiusmod tempo Lorem ipsum dolor sit amet, consectetur adipisicing elit....</p>
    <span class="cta" style="left:9px;top:88px;font-size:15px;letter-spacing:-.4px">DOWNLOAD TERMS &amp; CONDITIONS</span>
    <span class="doc-icon" style="left:266px;top:78px;width:30px;background:#2b8a3e;height:30px"></span>
  </section>

  <aside class="abs side-panel" style="top:518px">
    <div class="side-head" style="padding-left:78px">Online Surveys</div>
    <div class="survey-body">
      <p>What is your favorite color?</p>
      <ul><li>Red</li><li>Yellow</li><li>Green</li><li>White</li><li>Black</li></ul>
      <div class="submit">Submit</div>
    </div>
  </aside>

  <aside class="abs side-panel" style="top:804px">
    <div class="side-head" style="text-align:center;height:39px;line-height:39px">Promotional Items</div>
    <div class="promo-body">
      <div class="promo-item"><span class="thumb" role="img" aria-label="Clock product image"></span><h4>ATOM- UHR:</h4><p>Dies ist ein Typoblindtext. An ihm kann ob alle Buchstaben da sind und wie sie</p></div>
      <div class="promo-item"><span class="thumb" role="img" aria-label="Storage device product image"></span><h4>50GB SPEICHER KAPAZITÄT:</h4><p>Dies ist ein Typoblindtext. An ihm kann ob alle Buchstaben da sind und wie sie</p></div>
      <div class="promo-item"><span class="thumb" role="img" aria-label="Wrench tool image"></span><h4>VIELE EINSTELLUNGEN:</h4><p>Dies ist ein Typoblindtext. An ihm kann ob alle Buchstaben da sind und wie sie</p></div>
    </div>
  </aside>
</main>

<footer class="abs footer">Copyright @ 2011 Parcelwind.au. All Rights Reserved.</footer>
</body>
</html>
```